Lotus Path Acupuncture Business Card Design

I would like a business card design for my acupuncture business which is based from 2 practices in Melbourne, Australia.

The front of the card should include:

*The Logo
* Name - Marina Delacourt (B.App.Sc.(TCM), Dip.Rem.Mass.). (I would like the letters after my name in slightly smaller font)
* Mobile number - 0427 318 904
* Web address - www.lotuspathacu.com.au

On the back of the card I would somehow like to fit my 2 clinic addresses in. They are:

The Vital Balance Rooms
842 Brindle St, Camberwell VIC 3124
Ph: 1300 274 518

Harmony & Eastern Herbal Healing Centre
62 Wexcombe Rd, Malvern East VIC 3145
Ph: (03) 9871 3402

If there is space, I'd also like to add to the back of the card - Next Appointment............................ (or something along those lines).

Thanks and happy designing!

Target Market(s)

Health consumers, and colleagues in the health industry

Industry/Entity Type

Clinic

Contact Information for Business Card

as above in brief

Requirements
Must have
• I've seen some ok designs coming in, however I'd like to avoid the generic look with the added curved line details etc. I don't particularly need extra patterns added to the card. I'd prefer it to look quite clean and simple, and using more earthy colours (I'm not super keen on the lime green that a lot of designs seem to include. I don't mind the full black or white look, (obviously the back side needs to be a lighter colour to allow me to write appointment details on it). I also quite like the idea of the background looking like brown recycled paper (just an idea - that's not 100% necessary).
Nice to have
• I have an idea that I could have the main flower part of the logo printed as metallic.
Should not have
• Generic patterns and too much added detail.

```html
<!DOCTYPE html>
<html lang="en">
<head>
<meta charset="utf-8">
<title>Lotus Path Acupuncture – Business Card</title>
<link rel="stylesheet" href="https://fonts.googleapis.com/css2?family=Arimo:wght@400;700&display=swap">
<style>
  :root{
    --bg:#6f7378;
    --ink:#141210;
    --kraft:#c8a97e;
    --kraft-light:#e6d6bb;
    --bronze:#a8773f;
    --gold:#d9bf85;
    --white:#fbf9f5;
    --text:#2b241d;
    --rule:#9a8f80;
  }
  *{box-sizing:border-box;margin:0;padding:0}
  html,body{width:1200px;height:960px;overflow:hidden}
  body{background:var(--bg);font-family:"Arimo",sans-serif;position:relative}
  .card{position:absolute;top:160px;width:380px;height:640px;overflow:hidden;box-shadow:0 10px 30px rgba(0,0,0,.35)}
  .card-front{left:170px;background:var(--ink)}
  .card-back{left:650px;background:var(--white)}
  .card svg.shape{position:absolute;inset:0;width:380px;height:640px}

  /* front */
  .front-contact{position:absolute;top:34px;right:30px;text-align:right;color:var(--gold);font-size:17px;line-height:1}
  .front-contact .phone{margin-top:62px;font-size:19px}
  .brand{position:absolute;color:var(--gold);font-weight:400;text-align:center;line-height:1.15}
  .brand-front{top:172px;left:90px;width:200px;font-size:26px;display:flex;flex-direction:column;align-items:center;gap:10px}
  .brand-dot{width:14px;height:14px;border-radius:50%;background:var(--bronze)}
  .holder{position:absolute;left:26px;top:520px;color:var(--ink)}
  .holder .name{font-weight:700;font-size:25px}
  .holder .quals{font-weight:700;font-size:13px;margin-top:6px}

  /* back */
  .appt{position:absolute;top:36px;left:28px;right:26px}
  .appt-label{color:var(--bronze);font-weight:700;font-size:17px}
  .appt-line{height:0;border-bottom:1.5px solid var(--rule);margin-top:30px}
  .appt-line + .appt-line{margin-top:34px}
  .clinics{position:absolute;top:178px;left:28px;right:20px}
  .clinic + .clinic{margin-top:18px}
  .clinic-name{color:var(--bronze);font-weight:700;font-size:17px;line-height:1.2}
  .clinic-line{font-size:15px;color:var(--text);line-height:1.35;display:flex;align-items:center;gap:6px}
  .clinic-line .icon{width:12px;height:12px;flex:none}
  .clinic-line.addr{padding-left:18px}
  .brand-back{left:115px;top:450px;width:160px;height:160px;border-radius:50%;background:var(--ink);color:var(--gold);display:flex;align-items:center;justify-content:center;font-size:20px;padding:20px}
</style>
</head>
<body>

<section class="card card-front" aria-label="Card front">
  <svg class="shape" viewBox="0 0 380 640" aria-hidden="true">
    <path d="M0,266 C140,260 205,405 250,505 S320,640 342,640 L0,640 Z" fill="var(--kraft)"/>
  </svg>
  <div class="front-contact">
    <p class="web">www.lotuspathacu.com.au</p>
    <p class="phone">0427 318 904</p>
  </div>
  <div class="brand brand-front">
    <span class="brand-dot"></span>
    <span>Lotus Path Acupuncture</span>
  </div>
  <div class="holder">
    <p class="name">Marina Delacourt</p>
    <p class="quals">(B.App.Sc.(TCM), Dip.Rem.Mass.)</p>
  </div>
</section>

<section class="card card-back" aria-label="Card back">
  <svg class="shape" viewBox="0 0 380 640" aria-hidden="true">
    <path d="M0,415 C105,407 185,477 245,527 S348,597 380,568 L380,640 L0,640 Z" fill="var(--kraft-light)"/>
  </svg>
  <div class="appt">
    <p class="appt-label">Next appointment</p>
    <div class="appt-line"></div>
    <div class="appt-line"></div>
  </div>
  <div class="clinics">
    <div class="clinic">
      <p class="clinic-name">The Vital Balance Rooms</p>
      <p class="clinic-line addr">842 Brindle St, Camberwell VIC 3124</p>
      <p class="clinic-line"><svg class="icon" viewBox="0 0 12 12"><path d="M3 1 L5 3 L4 5 Q5 7 7 8 L9 7 L11 9 L9 11 Q3 10 1 3 Z" fill="var(--text)"/></svg>1300 274 518</p>
    </div>
    <div class="clinic">
      <p class="clinic-name">Harmony &amp; Eastern Herbal Healing Centre</p>
      <p class="clinic-line addr">62 Wexcombe Rd, Malvern East VIC 3145</p>
      <p class="clinic-line"><svg class="icon" viewBox="0 0 12 12"><path d="M3 1 L5 3 L4 5 Q5 7 7 8 L9 7 L11 9 L9 11 Q3 10 1 3 Z" fill="var(--text)"/></svg>(03) 9871 3402</p>
    </div>
  </div>
  <div class="brand brand-back">Lotus Path Acupuncture</div>
</section>

</body>
</html>
```